Business Card Design for a Software Startup

We'd like to have a business card design. We already have a logo. Basically what we need is a clean design with name, address, cellphone and phone numbers, e-mail and web site address (front) and a space on the back with our logo with the company name on the right side and some texts on the bottom.
We are a development and consulting company in Brazil with highly qualified team of professionals in Java, iOS and Android development and consulting.

Target Market(s)

CIO, IT managers of mid to big size companies

Industry/Entity Type

Business

```html
<!DOCTYPE html>
<html lang="en">
<head>
<meta charset="utf-8">
<title>ZENTORQ Business Card</title>
<link rel="stylesheet" href="https://fonts.googleapis.com/css2?family=Montserrat:wght@600;700&family=Questrial&display=swap">
<style>
  :root {
    --stage: #e9eaee;
    --blue-light: #0d9ad8;
    --blue-mid: #1584c4;
    --blue-deep: #1d6ca8;
    --navy: #1f3560;
    --accent-blue: #176aa6;
    --grey-bar: #9a9ea3;
    --paper: #f8f9fb;
    --text-grey: #4a5060;
  }
  * { margin: 0; padding: 0; box-sizing: border-box; }
  html, body { width: 1200px; height: 934px; overflow: hidden; }
  body {
    background: var(--stage);
    font-family: "Questrial", "Century Gothic", sans-serif;
    position: relative;
  }
  .card {
    position: absolute;
    top: 312px;
    width: 540px;
    height: 309px;
    overflow: hidden;
    box-shadow: 0 6px 18px rgba(0,0,0,0.12);
  }
  .card--back { left: 40px; background: linear-gradient(160deg, var(--blue-light), var(--blue-mid)); }
  .card--front { left: 620px; background: var(--paper); }

  .card__bands { position: absolute; inset: 0; }

  .brand { position: absolute; display: flex; align-items: center; gap: 12px; white-space: nowrap; }
  .brand__mark { display: block; border-radius: 6px; flex: none; }
  .brand__name {
    font-family: "Montserrat", sans-serif;
    font-weight: 700;
    letter-spacing: 1px;
    line-height: 1;
  }
  .card--back .brand { left: 38px; top: 44px; }
  .card--back .brand__mark { width: 44px; height: 44px; background: #ffffff; }
  .card--back .brand__name { color: #ffffff; font-size: 40px; }

  .card--front .brand { right: 24px; top: 68px; }
  .card--front .brand__mark { width: 56px; height: 56px; background: var(--accent-blue); }
  .card--front .brand__name { color: var(--navy); font-size: 48px; }

  .edge-tab { position: absolute; left: 0; top: 150px; width: 14px; height: 44px; background: var(--accent-blue); }
  .edge-bar { position: absolute; left: 250px; right: 0; bottom: 0; height: 14px; background: var(--grey-bar); }

  .person { position: absolute; left: 30px; top: 226px; text-align: right; }
  .person__name { font-family: "Montserrat", sans-serif; font-weight: 700; font-size: 15px; color: var(--navy); letter-spacing: 0.5px; }
  .person__role { font-size: 13px; color: var(--text-grey); margin-top: 2px; }

  .address { position: absolute; left: 196px; top: 208px; font-size: 13px; line-height: 17px; color: var(--text-grey); font-style: normal; }

  .divider { position: absolute; left: 330px; top: 208px; width: 1px; height: 34px; background: #c5c8cf; }

  .contact { position: absolute; left: 344px; top: 206px; list-style: none; font-size: 13px; line-height: 19px; color: var(--text-grey); }
  .contact li { display: flex; align-items: center; gap: 7px; white-space: nowrap; }
  .contact svg { width: 11px; height: 11px; fill: none; stroke: var(--accent-blue); stroke-width: 1.6; }
</style>
</head>
<body>

<div class="card card--back">
  <svg class="card__bands" viewBox="0 0 540 309" preserveAspectRatio="none" aria-hidden="true">
    <polygon points="300,309 540,40 540,110 380,309" fill="#1a6eae" opacity="0.55"/>
    <polygon points="420,309 540,170 540,230 480,309" fill="#1a6eae" opacity="0.5"/>
    <polygon points="230,309 500,0 540,0 540,20 300,309" fill="#1d6aa6" opacity="0.35"/>
  </svg>
  <div class="brand">
    <span class="brand__mark"></span>
    <span class="brand__name">ZENTORQ</span>
  </div>
</div>

<div class="card card--front">
  <div class="brand">
    <span class="brand__mark"></span>
    <span class="brand__name">ZENTORQ</span>
  </div>

  <span class="edge-tab"></span>
  <span class="edge-bar"></span>

  <div class="person">
    <div class="person__name">CAIO ANDRADE</div>
    <div class="person__role">Manager</div>
  </div>

  <address class="address">
    Av. Rio Claro<br>
    Centro - Campinas
  </address>

  <span class="divider"></span>

  <ul class="contact">
    <li>
      <svg viewBox="0 0 12 12"><rect x="3" y="0.8" width="6" height="10.4" rx="1"/><line x1="5" y1="9.3" x2="7" y2="9.3"/></svg>
      +55 11 4000 5120
    </li>
    <li>
      <svg viewBox="0 0 12 12"><rect x="0.8" y="2.2" width="10.4" height="7.6"/><polyline points="0.8,2.2 6,6.6 11.2,2.2"/></svg>
      info@zentorqit.com
    </li>
  </ul>
</div>

</body>
</html>
```